2020-23 Strategic Plan - Graphic Design Work

We would would like to have our strategic plan designed. It should be two pages.

- I am looking for suggestions on ways to lay this out. I don’t like this boxy layout. It was great for the committee as we went through multiple versions, but I’d prefer the final not follow this boxy format

- I’ve included a few images we own (feel free to use any or none of them). Also attached our logo.

- Have a look at our new website to see our new branding look and feel (launching next week) https://thevorlenta.example-hub.com/

- I've included a copy of our logo.

Target Market(s)

Membership

Other font styles liked:
• Lato

Requirements
Must have
• Excellent layout. Easy to ready. Consistent with branding.

```html
<!DOCTYPE html>
<html lang="en">
<head>
<meta charset="utf-8">
<title>Vorlenta Strategic Plan – Pillars</title>
<link href="https://fonts.googleapis.com/css2?family=Montserrat:wght@500;700&display=swap" rel="stylesheet">
<style>
  :root {
    --green: #4a9334;
    --white: #ffffff;
    --photo-light: #d9c7b4;
    --photo-mid: #a88a6c;
    --photo-dark: #4a3628;
  }
  * { box-sizing: border-box; margin: 0; padding: 0; }
  html, body { width: 1200px; height: 676px; overflow: hidden; }
  body { font-family: "Montserrat", sans-serif; color: var(--white); }
  .plan {
    position: relative;
    width: 1200px; height: 676px;
    background: var(--green);
    overflow: hidden;
  }
  .pillar {
    position: absolute;
    top: 39px;
    width: 184px;
    hyphens: auto;
    -webkit-hyphens: auto;
  }
  .pillar--educate { left: 45px; }
  .pillar--grow { left: 261px; }
  .pillar--lead { left: 480px; }
  .pillar--govern { left: 699px; }
  .pillar__icon {
    width: 87px; height: 87px;
    border: 2px solid var(--white);
    border-radius: 50%;
    display: flex; align-items: center; justify-content: center;
  }
  .pillar__icon svg { width: 32px; height: 32px; }
  .pillar__title {
    font-size: 17.5px; font-weight: 700;
    margin-top: 20px; line-height: 22px;
  }
  .pillar__label {
    font-size: 11.4px; font-weight: 700;
    margin-top: 22px; line-height: 14px;
  }
  .pillar__label + p { margin-top: 6px; }
  .pillar p, .pillar li {
    font-size: 11.6px; font-weight: 500;
    line-height: 12.5px;
  }
  .pillar p + p { margin-top: 12.5px; }
  .pillar__label--after { margin-top: 21px; }
  .actions { list-style: none; margin-top: 6px; }
  .actions li {
    position: relative;
    padding-left: 9px;
    margin-bottom: 6px;
  }
  .actions li::before {
    content: "•";
    position: absolute; left: 0; top: 0;
  }
  .photo {
    position: absolute;
    left: 912px; top: 0;
    width: 288px; height: 676px;
    background: linear-gradient(160deg, var(--photo-light) 0%, var(--photo-mid) 45%, var(--photo-dark) 100%);
  }
  .brand {
    position: absolute;
    left: 986px; top: 598px;
    display: flex; align-items: center; gap: 8px;
    color: var(--white);
    font-size: 22px; font-weight: 700; line-height: 26px;
  }
  .brand__dot {
    width: 20px; height: 20px;
    border-radius: 50%;
    background: var(--white);
  }
</style>
</head>
<body>
<main class="plan">

  <section class="pillar pillar--educate">
    <div class="pillar__icon">
      <svg viewBox="0 0 32 32" fill="none" stroke="#fff" stroke-width="2" stroke-linejoin="round">
        <path d="M3 7 h3 v18 h-3 z M6 6 c4 -1 7 0 10 2 v18 c-3 -2 -6 -3 -10 -2 z M26 6 c-4 -1 -7 0 -10 2 v18 c3 -2 6 -3 10 -2 z M26 7 h3 v18 h-3"/>
      </svg>
    </div>
    <h2 class="pillar__title">Educate</h2>
    <h3 class="pillar__label">Strategic Objective</h3>
    <p>Be the most trusted, relevant, and accessible provider of education and credentials in the field of property assessment in Canada</p>
    <h3 class="pillar__label pillar__label--after">Strategic Goals</h3>
    <p>Ensure a catalogue of relevant, high-quality courses, which meet the evolving needs of assessment professionals</p>
    <p>Provide an equal Vorlenta member experience and service, regardless of geography</p>
    <h3 class="pillar__label pillar__label--after">Sample Supporting Actions</h3>
    <ul class="actions">
      <li>Utilize technology to offer interactive and accessible online events</li>
      <li>Develop provincial legislation-specific content for Vorlenta courses</li>
      <li>Lead opportunities for collaboration across districts to increase access to quality PD opportunities</li>
    </ul>
  </section>

  <section class="pillar pillar--grow">
    <div class="pillar__icon">
      <svg viewBox="0 0 32 32" fill="none" stroke="#fff" stroke-width="3" stroke-linecap="round" stroke-linejoin="round">
        <path d="M3 22 l9 -8 l6 5 l10 -10 M20 9 h8 v8"/>
      </svg>
    </div>
    <h2 class="pillar__title">Grow</h2>
    <h3 class="pillar__label">Strategic Objective</h3>
    <p>Increase Vorlenta’s membership by serving all career levels and forging strong strategic partnerships.</p>
    <h3 class="pillar__label pillar__label--after">Strategic Goals</h3>
    <p>Enhance opportunities for senior assessment professionals through the VCF designation.</p>
    <p>Connect with young professionals by enhancing member communications, improving member onboarding, and expanding scholarship opportunities.</p>
    <h3 class="pillar__label pillar__label--after">Sample Supporting Actions</h3>
    <ul class="actions">
      <li>Develop framework for a specialist designation track</li>
      <li>Work collaboratively with strategic partners from across the country to develop criteria for, and launch, the VCF designation</li>
      <li>Redesign the new member onboarding experience</li>
    </ul>
  </section>

  <section class="pillar pillar--lead">
    <div class="pillar__icon">
      <svg viewBox="0 0 32 32" fill="none" stroke="#fff" stroke-width="2.2" stroke-linejoin="round">
        <path d="M8 29 V4 h16 l-4 6 l4 6 H8"/>
      </svg>
    </div>
    <h2 class="pillar__title">Lead</h2>
    <h3 class="pillar__label">Strategic Objective</h3>
    <p>Strengthen the reputation of the organization and its members by acting as a leader within the field of property assessment in Canada</p>
    <h3 class="pillar__label pillar__label--after">Strategic Goals</h3>
    <p>Embrace the role of leader and advocate within the property assessment profession</p>
    <p>Strengthen current, and develop new, strategic partnerships with peer associations across Canada.</p>
    <h3 class="pillar__label pillar__label--after">Sample Supporting Actions</h3>
    <ul class="actions">
      <li>Adopt an advocacy voice for the assessment profession to ensure interests are being represented</li>
      <li>Work with strategic partners to produce industry white papers with national relevance</li>
      <li>Engage with various levels of government across Canada</li>
    </ul>
  </section>

  <section class="pillar pillar--govern">
    <div class="pillar__icon">
      <svg viewBox="0 0 32 32" fill="none" stroke="#fff" stroke-width="2" stroke-linecap="round">
        <path d="M15 5 c-3 -1 -6 1 -6 4 c-3 1 -4 4 -3 6 c-2 2 -1 6 2 7 c0 3 3 5 7 4 z M17 5 c3 -1 6 1 6 4 c3 1 4 4 3 6 c2 2 1 6 -2 7 c0 3 -3 5 -7 4 z M11 12 c2 0 3 1 3 3 M21 12 c-2 0 -3 1 -3 3 M10 19 c2 -1 4 0 4 2 M22 19 c-2 -1 -4 0 -4 2"/>
      </svg>
    </div>
    <h2 class="pillar__title">Govern</h2>
    <h3 class="pillar__label">Strategic Objective</h3>
    <p>Fortify the future of Vorlenta through operational excellence and a diverse group of talented volunteers</p>
    <h3 class="pillar__label pillar__label--after">Strategic Goals</h3>
    <p>Review and align association management practices with strategic objectives and statements of Vision, Mission and Values.</p>
    <p>Secure Vorlenta’s financial stability by reviewing current pricing model and practicing sound risk management.</p>
    <h3 class="pillar__label pillar__label--after">Sample Supporting Actions</h3>
    <ul class="actions">
      <li>Align the Vorlenta budget and staffing needs to achieve clear strategic objectives</li>
      <li>Utilize automation to modernize systems and administrative processes</li>
      <li>Review and assess the relevance of current committees to determine if sufficient to meet the requirements of the strategic plan, and create new committees if deemed relevant</li>
    </ul>
  </section>

  <div class="photo" role="img" aria-label="Photo of a professional wearing a headset and glasses, working at a laptop and taking notes"></div>

  <div class="brand">
    <span class="brand__dot"></span>
    <span class="brand__name">Vorlenta</span>
  </div>

</main>
</body>
</html>
```